Flyer Design Project with ongoing regular work

We are a home delivery Company who specialise in two man home delivery of furniture for retail and trade businesses direct to the end user / customer. We need a sales flyer designed to start an ongoing regular campaign with different styles based on target customers. Our first 'batch' of printed flyers to be sent out will be aimed at companies based in Scotland requiring delivery throughout Scotland. and our second batch will be aimed at English Companies requiring delivery throughout Scotland. Although we deliver nationally we are keen to focus on the "Delivery throughout Scotland" aspect of our business, particularly for companies based in England and want to highlight this service. We want to give the impression of being a larger company and not a 'van & man' type business. with heavy emphasis on the high standards, professionalism and customer services. The design needs to be such that it will attract the attention of the recipient and not immediately thrown in the bin as junk mail. This ongoing campaign will require email templates to be created based on the printed flyers for follow up emails etc as part of an additional electronic campaign. Flyers will be printed onto decent quality card to enhance first impressions etc and add to overall sense of high end service. This project will be first of many for chosen designer as we expect to trial different styles and formats continually throughout this year. Our current website can be found at www.hauloriva.com We have already had logo designed by PlanMosaic member and have uploaded final copy files. The preferred logo is the one currently used on our website

Target Market(s)

Retailers, Internet Companies, and Manufacturers within the furniture industry who offer their customers home delivery by two men

Industry/Entity Type

Electronic

Requirements
Must have
• focus on "Delivery throughout Scotland" - Specialists in Scotland., We've got Scotland covered etc
Nice to have
• confident, vibrant enthusiastic feel, Quality & substance over quantity. We do not want to compete on price. We don't do cheap deliveries because we are much better than other companies of this type. Do not want to appear desperate for the work, rather more of a case of you get what you pay for. We dont want to attract clients who are looking for cheap options but likewise do not want to appear too expensive for potential new clients
Should not have
• items or images that suggest we are a "van & man" company or very small

```html
<!DOCTYPE html>
<html lang="en">
<head>
<meta charset="utf-8">
<title>Hauloriva – Scotland Delivery Flyer</title>
<link rel="stylesheet" href="https://fonts.googleapis.com/css2?family=Roboto+Condensed:wght@300;400;700&family=Roboto+Slab:wght@700;800&display=swap">
<style>
  :root {
    --canvas: #eceef1;
    --paper: #ffffff;
    --navy: #0d3a78;
    --blue: #1f63b5;
    --sky: #4fa6e3;
    --ice: #dcebf7;
    --slate: #5b7896;
    --ink: #3a3f45;
    --grey-swoosh: #c8d2dc;
    --accent-green: #6cb33f;
  }
  * { margin: 0; padding: 0; box-sizing: border-box; }
  html, body { width: 1200px; height: 847px; overflow: hidden; }
  body {
    background: var(--canvas);
    font-family: "Roboto Condensed", "Arial Narrow", sans-serif;
    color: var(--ink);
    position: relative;
  }
  .flyer {
    position: absolute;
    top: 33px;
    width: 552px;
    height: 780px;
    background: var(--paper);
    box-shadow: 0 4px 18px rgba(20, 40, 70, 0.18);
    overflow: hidden;
  }
  .flyer--front { left: 30px; }
  .flyer--back { left: 618px; }
  .flyer__art { position: absolute; inset: 0; width: 100%; height: 100%; }

  /* Front */
  .intro {
    position: absolute;
    left: 62px; top: 30px; width: 200px;
    color: #fff;
    font-size: 14px; line-height: 1.33; font-weight: 300;
  }
  .intro p + p { margin-top: 16px; }
  .headline {
    position: absolute;
    left: 62px; top: 600px;
    color: var(--slate);
    font-weight: 300; font-size: 30px; line-height: 1.08;
    text-transform: uppercase;
  }
  .headline strong {
    display: block;
    font-family: "Roboto Slab", Georgia, serif;
    font-weight: 800; font-size: 31px;
    color: var(--navy);
    letter-spacing: 0.5px;
    margin-top: 2px;
  }

  .brand {
    position: absolute;
    display: flex; align-items: center; gap: 7px;
    font-family: "Roboto Condensed", "Arial Narrow", sans-serif;
    font-weight: 700; font-size: 24px;
    color: var(--blue);
  }
  .brand__dot {
    width: 18px; height: 18px; border-radius: 50%;
    background: var(--accent-green);
  }
  .flyer--front .brand { left: 58px; top: 722px; }
  .flyer--back .brand { left: 308px; top: 722px; }

  /* Back */
  .section-tag {
    position: absolute;
    left: 70px; top: 40px;
    transform: rotate(-7deg);
    transform-origin: left center;
    color: var(--navy);
    font-size: 17px; font-weight: 400;
    white-space: nowrap;
  }
  .section-tag strong {
    font-family: "Roboto Slab", Georgia, serif;
    font-weight: 800; font-size: 23px;
    text-transform: uppercase;
  }
  .details {
    position: absolute;
    top: 336px; left: 70px; right: 48px;
    display: grid;
    grid-template-columns: 208px 1fr;
    column-gap: 26px;
    font-size: 12.6px; line-height: 1.38;
    color: var(--ink);
  }
  .details__col > * + * { margin-top: 14px; }
  .services { list-style: none; }
  .services li::before { content: "• "; }
  .services li { padding-left: 8px; text-indent: -8px; }
  .details h3 {
    font-family: "Roboto Slab", Georgia, serif;
    font-weight: 700; font-size: 12.5px;
    text-transform: uppercase;
    color: var(--navy);
    letter-spacing: 0.3px;
    margin-bottom: 3px;
  }
</style>
</head>
<body>

<section class="flyer flyer--front" aria-label="Flyer front">
  <svg class="flyer__art" viewBox="0 0 552 780">
    <defs>
      <linearGradient id="front-sky" x1="0" y1="0" x2="1" y2="1">
        <stop offset="0" stop-color="#2f7fce"/>
        <stop offset="0.5" stop-color="#1a5aab"/>
        <stop offset="1" stop-color="#0f3f86"/>
      </linearGradient>
      <linearGradient id="front-bridge" x1="0" y1="0" x2="0" y2="1">
        <stop offset="0" stop-color="#1b3f7a"/>
        <stop offset="0.55" stop-color="#c46a2a"/>
        <stop offset="1" stop-color="#243a66"/>
      </linearGradient>
      <linearGradient id="front-paper" x1="0" y1="0" x2="0" y2="1">
        <stop offset="0.6" stop-color="#ffffff"/>
        <stop offset="1" stop-color="#e8ecf0"/>
      </linearGradient>
      <linearGradient id="panel" x1="0" y1="0" x2="0" y2="1">
        <stop offset="0" stop-color="#ffffff" stop-opacity="0.16"/>
        <stop offset="1" stop-color="#ffffff" stop-opacity="0"/>
      </linearGradient>
      <radialGradient id="photo-road" cx="0.5" cy="0.5" r="0.6">
        <stop offset="0" stop-color="#f4e7c2"/>
        <stop offset="1" stop-color="#6f7f8c"/>
      </radialGradient>
      <radialGradient id="photo-fleet" cx="0.5" cy="0.5" r="0.6">
        <stop offset="0" stop-color="#e9eef3"/>
        <stop offset="1" stop-color="#5d7590"/>
      </radialGradient>
    </defs>

    <rect width="552" height="780" fill="url(#front-paper)"/>
    <path d="M0 0H552V430C430 500 250 560 0 575Z" fill="url(#front-sky)"/>
    <rect x="48" y="0" width="226" height="340" fill="url(#panel)"/>

    <path role="img" aria-label="Photograph of a lit railway bridge over water at dusk"
          d="M0 410C170 440 370 420 552 332V430C430 500 250 560 0 575Z" fill="url(#front-bridge)"/>

    <path d="M0 398C180 432 380 410 552 318" fill="none" stroke="#ffffff" stroke-width="7"/>
    <path d="M0 384C190 416 390 392 552 296" fill="none" stroke="#58b4ee" stroke-width="3" opacity="0.8"/>
    <path d="M0 586C250 570 430 510 552 442" fill="none" stroke="var(--grey-swoosh)" stroke-width="16"/>
    <path d="M0 575C250 560 430 500 552 430" fill="none" stroke="#2c73c4" stroke-width="4"/>

    <circle cx="470" cy="72" r="62" fill="#9fd2f2"/>
    <circle role="img" aria-label="Photograph of a motorway in motion blur" cx="470" cy="72" r="55" fill="url(#photo-road)"/>
    <circle cx="438" cy="218" r="62" fill="#9fd2f2"/>
    <circle role="img" aria-label="Photograph of a fleet of delivery lorries" cx="438" cy="218" r="55" fill="url(#photo-fleet)"/>
  </svg>

  <div class="intro">
    <p>Hauloriva provide Trade Distribution and Home Delivery Services to the Furniture Industry throughout the UK. We offer a full logistics solution and cater to companies of all sizes, from single unit retailers, Internet companies, retail chains and multiples to importers, suppliers and large manufacturers.</p>
    <p>Hauloriva specialise in “2 Man Home Delivery” services.</p>
  </div>

  <h1 class="headline">Specialist in<br>delivery throughout<strong>Scotland</strong></h1>

  <div class="brand"><span class="brand__dot"></span>Hauloriva</div>
</section>

<section class="flyer flyer--back" aria-label="Flyer back">
  <svg class="flyer__art" viewBox="0 0 552 780">
    <defs>
      <linearGradient id="back-head" x1="0" y1="0" x2="1" y2="0">
        <stop offset="0" stop-color="#e9f1f8"/>
        <stop offset="1" stop-color="#bcd6ec"/>
      </linearGradient>
      <linearGradient id="back-strip" x1="0" y1="0" x2="1" y2="0">
        <stop offset="0" stop-color="#3d6aa0"/>
        <stop offset="0.45" stop-color="#d7dde4"/>
        <stop offset="1" stop-color="#b89466"/>
      </linearGradient>
      <linearGradient id="back-swoosh" x1="0" y1="0" x2="1" y2="0">
        <stop offset="0" stop-color="#0e3e85"/>
        <stop offset="1" stop-color="#3c95dc"/>
      </linearGradient>
      <linearGradient id="back-paper" x1="0" y1="0" x2="0" y2="1">
        <stop offset="0.55" stop-color="#ffffff"/>
        <stop offset="1" stop-color="#e6ebf0"/>
      </linearGradient>
      <radialGradient id="map-disc" cx="0.4" cy="0.4" r="0.7">
        <stop offset="0" stop-color="#cfe6f7"/>
        <stop offset="1" stop-color="#2a6fbf"/>
      </radialGradient>
    </defs>

    <rect width="552" height="780" fill="url(#back-paper)"/>
    <path d="M0 0H552V100C380 40 200 60 0 112Z" fill="url(#back-head)"/>
    <path d="M0 112C200 60 380 40 552 100" fill="none" stroke="#1f63b5" stroke-width="3"/>

    <path role="img" aria-label="Photographs of a warehouse, a delivery lorry and stacked cardboard boxes"
          d="M0 112C200 60 380 40 552 100V286C400 244 200 252 0 312Z" fill="url(#back-strip)"/>

    <path d="M0 330C200 266 400 260 552 300V286C400 244 200 252 0 312Z" fill="url(#back-swoosh)"/>
    <path d="M0 342C200 280 400 274 552 314" fill="none" stroke="var(--grey-swoosh)" stroke-width="6"/>

    <circle cx="478" cy="62" r="62" fill="#ffffff" opacity="0.7"/>
    <circle role="img" aria-label="Map of Scotland" cx="478" cy="62" r="56" fill="url(#map-disc)"/>
  </svg>

  <div class="section-tag">Delivery Services in <strong>Scotland</strong></div>

  <div class="details">
    <div class="details__col">
      <ul class="services">
        <li>Furniture Installation</li>
        <li>Unpacking and waste removal</li>
        <li>Delivery window of 3 hours booked in advance</li>
      </ul>
      <div>
        <h3>Why Hauloriva</h3>
        <p>There are many reasons we are better than other delivery companies. We provide a more personal delivery with great attention to detail making every delivery that little bit better and we understand that the small things go a long way. Nothing is too much trouble for our staff who provide customer service that’s second to none. A fresh and helpful approach in everything we do helps to keep us ahead of crowd and we take great pride in the reputation we have built over the years for reliability, quality of service and customer satisfaction.</p>
      </div>
    </div>
    <div class="details__col">
      <ul class="services">
        <li>Two man home delivery service</li>
        <li>Room of choice &amp; placement</li>
        <li>Pre delivery courtesy call when vehicle is 1 hour away</li>
      </ul>
      <div>
        <h3>Where do deliver</h3>
        <p>Hauloriva provide services throughout the UK. Having our main hub near Kelvinmoor Park means that the majority of our delivery work is undertaken throughout Scotland, although almost 70% of this work is collected from Companies based in England. Our collection vehicles are in England every day and we have a number of satellite throughout England.</p>
      </div>
      <div>
        <h3>Contact us today</h3>
        <p>Two man home delivery services<br>0800 555 0142</p>
      </div>
    </div>
  </div>

  <div class="brand"><span class="brand__dot"></span>Hauloriva</div>
</section>

</body>
</html>
```